ALL TEXT GRAPHICS TM May 2025 for Instagram

We are looking for a series of social media graphics for Instagram (new size: 4:5 (1080 x 1350 pixels) ratio that are ALL TEXT. We want the following quotes below on each graphic; one quote per graphic. AND, In very small letters at the bottom of each graphic, add @TovaMarshOnline
The look and feel of these graphics should be complimentary to the color palette attached below; but keep them simple. But the design is up to you; at the end of this document, I provided various samples of all text graphics that I like as examples.
Target Market(s)
women looking to lose weight
Look and feel

```html
<!DOCTYPE html>
<html lang="en">
<head>
<meta charset="utf-8">
<title>All Text Graphics – TM May 2025</title>
<link rel="stylesheet" href="https://fonts.googleapis.com/css2?family=Outfit:wght@200;300;800;900&display=swap">
<style>
  :root {
    --bg: #dbdbdb;
    --card: #ffffff;
    --ink: #141414;
    --pink: #ff0a8c;
  }
  * { box-sizing: border-box; margin: 0; padding: 0; }
  html, body {
    width: 1200px; height: 849px; overflow: hidden;
    background: var(--bg);
    font-family: "Outfit", sans-serif;
    color: var(--ink);
  }
  .series { position: relative; width: 1200px; height: 849px; }
  .post {
    position: absolute; width: 218px; height: 272px;
    background: var(--card);
  }
  .row-1 { top: 141px; }
  .row-2 { top: 435px; }
  .col-1 { left: 37px; } .col-2 { left: 264px; } .col-3 { left: 491px; }
  .col-4 { left: 718px; } .col-5 { left: 945px; }

  .block { position: absolute; white-space: nowrap; }
  .headline { font-weight: 200; font-size: 27px; line-height: 30px; letter-spacing: 0.2px; }
  .accent { color: var(--pink); font-weight: 800; }
  .subhead { color: var(--pink); font-weight: 800; font-size: 18px; line-height: 20px; }
  .subhead-lg { color: var(--pink); font-weight: 800; font-size: 19px; line-height: 24px; }
  .body { font-weight: 300; font-size: 13.5px; line-height: 17.5px; letter-spacing: 0.2px; }
  .body .accent { font-weight: 800; }
  .footer { position: absolute; bottom: 12px; font-size: 13.5px; line-height: 17.5px; }
  .footer .cta { color: var(--pink); font-weight: 800; display: block; }
  .footer .handle { font-weight: 300; letter-spacing: 0.2px; display: block; }
  .mega { color: var(--pink); font-weight: 900; font-size: 88px; line-height: 1; letter-spacing: -2px; }
  .big { color: var(--pink); font-weight: 900; font-size: 45px; line-height: 1; }
  .tight { letter-spacing: -0.8px; }
  .list { font-weight: 300; font-size: 19px; line-height: 24px; }
  .list .accent { font-weight: 800; }
</style>
</head>
<body>
<main class="series">

  <section class="post row-1 col-1">
    <h2 class="block headline" style="left:43px;top:18px">Tired.<br>Moody.</h2>
    <p class="block subhead" style="left:43px;top:83px">Stubborn<br>Belly Fat.</p>
    <p class="block body" style="left:43px;top:142px">Your hormones are<br>screaming for help!</p>
    <p class="footer" style="left:43px"><span class="cta">Let's fix that.</span><span class="handle">@TovaMarshOnline</span></p>
  </section>

  <section class="post row-1 col-2">
    <h2 class="block headline" style="left:27px;top:18px">That<br>stubborn<br>weight?</h2>
    <p class="block subhead" style="left:27px;top:113px">It's not<br>your fault.</p>
    <p class="block body" style="left:27px;top:171px">Your hormones are to<br>blame and you're not<br>alone; <span class="accent">But there is a fix.</span></p>
    <p class="footer" style="left:27px"><span class="handle">@TovaMarshOnline</span></p>
  </section>

  <section class="post row-1 col-3">
    <h2 class="block headline" style="left:29px;top:18px">Your belly<br>isn't fat...</h2>
    <p class="block subhead" style="left:29px;top:83px">it's hormonal.</p>
    <p class="block body" style="left:29px;top:122px">And here's how to fix it.<br>Comment <span class="accent">HORMONES</span><br>if nothing is working.</p>
    <p class="footer" style="left:29px"><span class="handle">@TovaMarshOnline</span></p>
  </section>

  <section class="post row-1 col-4">
    <h2 class="block headline" style="left:20px;top:18px">The stubborn<br>belly fat after</h2>
    <p class="block mega" style="left:18px;top:76px">40?</p>
    <p class="block body" style="left:20px;top:159px">It's not about calories;<br>it's about your hormones.</p>
    <p class="footer" style="left:20px"><span class="cta">Here is the fix!</span><span class="handle">@TovaMarshOnline</span></p>
  </section>

  <section class="post row-1 col-5">
    <h2 class="block headline" style="left:14px;top:18px">Flat tummy<br>in <span class="accent">your 40s?</span></h2>
    <p class="block subhead" style="left:14px;top:83px">It's still possible!</p>
    <p class="block body" style="left:14px;top:122px">Comment <span class="accent">BYE BELLY</span> to get<br>the <span class="accent">10 secrets</span> to a flatter<br>tummy.</p>
    <p class="footer" style="left:14px"><span class="handle">@TovaMarshOnline</span></p>
  </section>

  <section class="post row-2 col-1">
    <h2 class="block headline" style="left:22px;top:18px">Bloating.<br>Muffin top.</h2>
    <p class="block subhead" style="left:22px;top:83px">It's still possible!</p>
    <p class="block subhead" style="left:22px;top:120px">Puffy waistline.</p>
    <p class="block body" style="left:22px;top:141px">Your body's screaming for<br>a different kind of fix.</p>
    <p class="footer" style="left:22px"><span class="cta">Here it is...</span><span class="handle">@TovaMarshOnline</span></p>
  </section>

  <section class="post row-2 col-2">
    <h2 class="block headline" style="left:9px;top:18px">You're doing<br>all the <span class="accent">“right”</span><br>things, but</h2>
    <p class="block subhead" style="left:9px;top:134px">your belly won't<br>go down?</p>
    <p class="footer" style="left:9px"><span class="cta">Here's what you haven't tried.</span><span class="handle">@TovaMarshOnline</span></p>
  </section>

  <section class="post row-2 col-3">
    <h2 class="block headline" style="left:17px;top:18px">This <span class="accent">90-day</span><br><span class="accent">plan</span> helped<br>women</h2>
    <p class="block list" style="left:17px;top:134px">over <span class="accent">40 slim down</span>,<br>get <span class="accent">a tiny waist</span><br>and <span class="accent">feel sexy again</span>.</p>
    <p class="footer" style="left:17px"><span class="cta">You're next.</span><span class="handle">@TovaMarshOnline</span></p>
  </section>

  <section class="post row-2 col-4">
    <h2 class="block headline" style="left:12px;top:18px">This is the<br>secret women</h2>
    <p class="block big" style="left:11px;top:76px">over 40</p>
    <p class="block body" style="left:12px;top:126px">are using to get snatched;<br>without starving.</p>
    <p class="block body" style="left:12px;top:183px">Comment <span class="accent">SKINNY</span><br>to get the exact plan.</p>
    <p class="footer" style="left:12px"><span class="handle">@TovaMarshOnline</span></p>
  </section>

  <section class="post row-2 col-5">
    <h2 class="block headline tight" style="left:12px;top:20px">What worked in</h2>
    <p class="block big" style="left:11px;top:52px">your 30s</p>
    <p class="block headline" style="left:12px;top:98px">won't work now.</p>
    <p class="block body" style="left:12px;top:141px">Here's what actually does.<br><span class="accent">Drop 30 Pounds in 3 Months.</span></p>
    <p class="footer" style="left:12px"><span class="handle">@TovaMarshOnline</span></p>
  </section>

</main>
</body>
</html>
```